Paws About Town Helpers

Design a flyer (A5 - I think!) with bright colours to promote an in home Dog Service.
Include an animated picture of a dog (being walked/playing/jumping etc)
Bold Heading, list of services with animated pictures, contact details

Industry/Entity Type

It Service

Requirements
Must have
• Add price list to back of A5 Flyer with same colours and design as front page of flyer - See Attached.

```html
<!DOCTYPE html>
<html lang="en">
<head>
<meta charset="utf-8">
<title>Paws About Town Helpers – Flyer</title>
<link rel="stylesheet" href="https://fonts.googleapis.com/css2?family=Lobster&family=Fjalla+One&family=Lato:wght@700;900&family=Oswald:wght@500;700&display=swap">
<style>
  :root{
    --royal:#1a2fd6;
    --navy:#0c1a9e;
    --sky-top:#5fb6ea;
    --sky-low:#cfeafa;
    --grass:#6cbf2e;
    --grass-dark:#3f9a1c;
    --sun:#ffd21a;
    --amber:#f7b500;
    --red:#e0242c;
    --red-dark:#b3121b;
    --ink:#1b1b1b;
    --white:#ffffff;
    --head-blue:#1437e0;
  }
  *{margin:0;padding:0;box-sizing:border-box}
  html,body{width:900px;height:1200px;overflow:hidden;background:#e9e9e9}
  .flyer{position:relative;width:900px;height:1200px;overflow:hidden;background:var(--royal)}
  .top-strip{position:absolute;left:0;top:0;width:900px;height:32px;background:var(--royal)}
  .hero-art{position:absolute;left:0;top:32px;width:900px;height:478px;
    background:linear-gradient(180deg,var(--sky-top) 0%,var(--sky-low) 42%,var(--grass) 60%,var(--grass-dark) 100%)}
  .headline{position:absolute;right:40px;top:215px;text-align:center;width:330px}
  .headline .we-are{display:block;font-family:'Lobster',cursive;font-size:84px;line-height:1;color:var(--head-blue);
    -webkit-text-stroke:3px var(--white);paint-order:stroke fill;text-shadow:0 3px 4px rgba(0,0,0,.35)}
  .headline .name-top{display:block;font-family:'Fjalla One',sans-serif;font-size:36px;color:var(--red);margin-top:6px;
    text-shadow:0 2px 2px rgba(255,255,255,.6)}
  .headline .name-main{display:block;font-family:'Fjalla One',sans-serif;font-size:82px;line-height:1.05;color:var(--sun);
    text-shadow:0 3px 3px rgba(0,0,0,.35)}
  .divider-band{position:absolute;left:0;top:510px;width:900px;height:24px;background:var(--royal)}
  .services-panel{position:absolute;left:0;top:534px;width:900px;height:600px;
    background:radial-gradient(circle at 25% 75%,#fff3a0 0%,var(--sun) 35%,var(--amber) 100%)}
  .footer-band{position:absolute;left:0;top:0;width:900px;height:1200px;pointer-events:none}
  .badge{position:absolute;left:57px;top:475px;width:255px;height:385px}
  .badge svg{position:absolute;inset:0}
  .badge-text{position:absolute;left:0;top:40px;width:255px;text-align:center;font-family:'Oswald',sans-serif}
  .badge-text .line1{display:block;color:var(--white);font-size:30px;font-weight:500;line-height:1.15}
  .badge-text .line2{display:block;color:#2a1a1a;font-size:34px;font-weight:700;line-height:1.1}
  .badge-text .line3{display:block;color:var(--white);font-size:32px;font-weight:500;line-height:1.2}
  .badge-text .line3 .dog{font-family:'Lobster',cursive;color:var(--sun);font-size:44px}
  .call-row{display:flex;align-items:center;justify-content:center;gap:10px;margin-top:14px}
  .phone-icon{width:54px;height:50px;background:var(--white);border-radius:6px;display:flex;align-items:center;justify-content:center}
  .call-words{text-align:left;font-family:'Lato',sans-serif;line-height:1}
  .call-words .call{display:block;color:var(--white);font-size:20px;font-weight:700}
  .call-words .today{display:block;color:#2a1a1a;font-size:27px;font-weight:900;font-family:'Oswald',sans-serif}
  .phone-number{display:block;margin-top:8px;font-family:'Fjalla One',sans-serif;font-size:40px;color:var(--sun);letter-spacing:1px}
  .puppy-photo{position:absolute;left:58px;top:880px;width:265px;height:225px;border-radius:46% 46% 24% 24%;
    background:radial-gradient(ellipse at 50% 40%,#f1dcb4 0%,#dcb98a 60%,#c59c67 100%)}
  .services{position:absolute;right:40px;top:560px;width:560px;text-align:right;list-style:none}
  .service{margin-bottom:16px}
  .service-q{display:flex;justify-content:flex-end;align-items:center;gap:8px;font-family:'Fjalla One',sans-serif;
    font-size:27px;line-height:1.05;color:var(--head-blue);text-transform:uppercase}
  .service-q .mark{font-family:'Oswald',sans-serif;font-weight:700;font-size:46px;color:var(--red);line-height:.9}
  .service-a{font-family:'Lato',sans-serif;font-weight:700;font-size:23px;line-height:1.3;color:var(--ink);margin-top:4px;padding-right:0}
  .website{position:absolute;left:0;top:1143px;width:900px;text-align:center;font-family:'Lato',sans-serif;font-weight:700;
    font-size:21px;letter-spacing:3px;color:var(--white)}
</style>
</head>
<body>
<main class="flyer">
  <div class="top-strip"></div>
  <div class="hero-art" role="img" aria-label="Cartoon of a brown dog leaping after a red frisbee thrown by a boy in a sunny green park"></div>

  <h1 class="headline">
    <span class="we-are">We Are</span>
    <span class="name-top">Paws About Town</span>
    <span class="name-main">Helpers</span>
  </h1>

  <div class="divider-band"></div>
  <div class="services-panel"></div>

  <svg class="footer-band" viewBox="0 0 900 1200" aria-hidden="true">
    <polygon points="0,1080 405,1080 455,1118 900,1118 900,1200 0,1200" fill="var(--royal)"/>
    <polygon points="405,1080 900,1080 900,1118 455,1118" fill="var(--amber)"/>
  </svg>

  <div class="puppy-photo" role="img" aria-label="Photo of a yellow Labrador puppy resting its paws on the edge"></div>

  <aside class="badge">
    <svg viewBox="0 0 255 385" aria-hidden="true">
      <polygon points="0,10 10,0 10,12" fill="var(--navy)"/>
      <polygon points="255,10 245,0 245,12" fill="var(--navy)"/>
      <defs>
        <linearGradient id="badgeFill" x1="0" y1="0" x2="0" y2="1">
          <stop offset="0" stop-color="#f0444a"/>
          <stop offset="1" stop-color="var(--red-dark)"/>
        </linearGradient>
      </defs>
      <polygon points="0,10 255,10 255,330 127,385 0,330" fill="url(#badgeFill)"/>
      <polygon points="12,22 243,22 243,322 127,371 12,322" fill="none" stroke="var(--white)" stroke-width="2" stroke-dasharray="6 4"/>
    </svg>
    <div class="badge-text">
      <span class="line1">For all Services</span>
      <span class="line2">RELATED TO</span>
      <span class="line3">YOUR <span class="dog">Dog</span></span>
      <div class="call-row">
        <span class="phone-icon">
          <svg width="34" height="30" viewBox="0 0 34 30" aria-hidden="true">
            <path d="M3 9c0-5 6-7 14-7s14 2 14 7v3h-8V8h-12v4H3z" fill="var(--head-blue)"/>
            <rect x="6" y="13" width="22" height="15" rx="3" fill="var(--head-blue)"/>
            <circle cx="17" cy="20.5" r="4" fill="var(--white)"/>
          </svg>
        </span>
        <span class="call-words"><span class="call">CALL PATH</span><span class="today">TODAY</span></span>
      </div>
      <span class="phone-number">0400 318 527</span>
    </div>
  </aside>

  <ul class="services">
    <li class="service">
      <div class="service-q"><span>Tired of picking up dog poop</span><span class="mark">?</span></div>
      <p class="service-a">Arrange for us to do it for you!</p>
    </li>
    <li class="service">
      <div class="service-q"><span>Need a break from walking<br>the dog</span><span class="mark">?</span></div>
      <p class="service-a">We will come and collect your dog and<br>take it for a walk!</p>
    </li>
    <li class="service">
      <div class="service-q"><span>Can’t get home in time to feed<br>your dog</span><span class="mark">?</span></div>
      <p class="service-a">Use our dog feeding service!</p>
    </li>
    <li class="service">
      <div class="service-q"><span>Want someone to play with<br>your dog while you’re at work</span><span class="mark">?</span></div>
      <p class="service-a">We will be Paws About Town Helpers!</p>
    </li>
    <li class="service">
      <div class="service-q"><span>Dog needs a bath</span><span class="mark">?</span></div>
      <p class="service-a">We’ll arrange for a professional to<br>keep it clean!</p>
    </li>
  </ul>

  <p class="website">www.pawsabouttownhelpers.com.au</p>
</main>
</body>
</html>
```